Design some Business Cards for Kelvo Systems

I need a design for business cards. I have an existing logo.

I am a sole trader (work for myself) and I provide computer and IT technology support services to small businesses in Australia. I advise business owners on how to best use and manage their IT systems and computers and I provide onsite computer troubleshooting services.
The style should reflect the professional nature of my work.
I would likely favour a simpler and clean design.

The artwork needs to be:
Single sided (just the front of the card)
89mm x 54mm in size.
Full colour.
To be printed on white stock (paper)

Details that need to be included on the business cards are:
Logo
Name Miles BBBBBBBB
Email address miles@kelvosys.example
Phone number 2222 222 222

The exact details will be supplied at the end of the contest for the final artwork.
Final artwork would need to be print ready – I can provide examples of what they need to look like.

```html
<!DOCTYPE html>
<html lang="en">
<head>
<meta charset="utf-8">
<title>Kelvo Systems – Business Card Concepts</title>
<link rel="stylesheet" href="https://fonts.googleapis.com/css2?family=Open+Sans:wght@400;600&display=swap">
<style>
  :root {
    --canvas: #ffffff;
    --card-white: #ffffff;
    --card-grey: #e6e7e9;
    --card-edge: #5b5d60;
    --ink: #2b2b2d;
    --ink-soft: #5a5c60;
    --brand-blue: #1f4fa8;
    --brand-blue-deep: #1b2a80;
    --brand-grey: #5e6064;
    --brand-grey-light: #9a9ca0;
  }
  * { box-sizing: border-box; margin: 0; padding: 0; }
  html, body {
    width: 898px; height: 1200px; overflow: hidden;
    background: var(--canvas);
    font-family: "Open Sans", Arial, sans-serif;
    color: var(--ink);
  }
  .sheet { position: relative; width: 898px; height: 1200px; }

  .card {
    position: absolute;
    border-radius: 30px;
    overflow: hidden;
    border: 1px solid #c9cacc;
    box-shadow: -4px 4px 0 var(--card-edge);
  }
  .card--white { left: 12px; top: 6px; width: 884px; height: 558px; background: var(--card-white); }
  .card--grey  { left: 4px;  top: 638px; width: 888px; height: 558px; background: var(--card-grey); }

  .card__graphic {
    position: absolute;
    left: 488px; top: -110px;
    width: 500px; height: 540px;
    border-radius: 50%;
    background: linear-gradient(200deg, var(--brand-grey-light) 0%, var(--brand-grey) 30%, var(--brand-blue-deep) 52%, var(--brand-blue) 70%, var(--brand-grey) 100%);
    opacity: .92;
  }

  .brand {
    position: absolute;
    display: flex; align-items: center; gap: 22px;
  }
  .card--white .brand { left: 68px; top: 116px; }
  .card--grey .brand  { left: 62px; top: 150px; }
  .brand__dot {
    width: 78px; height: 78px; border-radius: 50%;
    background: var(--brand-blue);
  }
  .brand__text { display: flex; flex-direction: column; }
  .brand__name {
    font-size: 36px; font-weight: 400; line-height: 1.1;
    color: var(--brand-blue);
    letter-spacing: -0.5px;
  }
  .brand__tagline {
    font-size: 11.5px; color: var(--ink-soft); margin-top: 2px; padding-left: 4px;
  }

  .contact {
    position: absolute;
    font-size: 22px; line-height: 28px;
    color: var(--ink);
  }
  .card--white .contact { left: 68px; top: 368px; }
  .card--grey .contact  { left: 68px; top: 366px; }
  .contact__label { margin-right: 6px; }
  .contact__name { font-size: 30px; }
  .contact__row--name { line-height: 38px; }
</style>
</head>
<body>
<main class="sheet">

  <section class="card card--white" aria-label="Business card, white version">
    <div class="card__graphic" role="img" aria-label="Large decorative swirl graphic in blue and grey"></div>
    <div class="brand">
      <span class="brand__dot"></span>
      <div class="brand__text">
        <span class="brand__name">Kelvo Systems</span>
        <span class="brand__tagline">Onsite IT Support for Business</span>
      </div>
    </div>
    <div class="contact">
      <p class="contact__row contact__row--name"><span class="contact__label">Name</span> <span class="contact__name">Miles BBBBBBBB</span></p>
      <p class="contact__row"><span class="contact__label">Email</span> miles@kelvosys.example</p>
      <p class="contact__row"><span class="contact__label">Phone</span> 2222 222 222</p>
      <p class="contact__row">www.kelvosys.example</p>
    </div>
  </section>

  <section class="card card--grey" aria-label="Business card, grey version">
    <div class="card__graphic" role="img" aria-label="Large decorative swirl graphic in blue and grey"></div>
    <div class="brand">
      <span class="brand__dot"></span>
      <div class="brand__text">
        <span class="brand__name">Kelvo Systems</span>
        <span class="brand__tagline">Onsite IT Support for Business</span>
      </div>
    </div>
    <div class="contact">
      <p class="contact__row contact__row--name"><span class="contact__label">Name</span> <span class="contact__name">Miles BBBBBBBB</span></p>
      <p class="contact__row"><span class="contact__label">Email</span> miles@kelvosys.example</p>
      <p class="contact__row"><span class="contact__label">Phone</span> 2222 222 222</p>
      <p class="contact__row">www.kelvosys.example</p>
    </div>
  </section>

</main>
</body>
</html>
```